Painting Valtoni Renovations New buildings

Paint jobs plasterwork renovations new building customer painter paper drywall Entsorgungen.neukunden win color splash pleasure in colors competent clean fast reliable new try build demolition color combinations color concepts offers washing façade painting wood stains new projects old building renovations yes no beautiful new old sell secure solve paint over paint paint spray paint lye assemble disassemble sell buy trade oil dust new old assembly disassembly putty sanding fashion devastation copying belief feng shui kleopatra pompes beer colors swamp lime abrasion release tighten

Target Market(s)

construction industry

Contact Information for Business Card

Maler

Font styles to use
Serif

Colors
f04a50
959595

Requirements
Must have
• elegant appearance
Nice to have
• simply goal-oriented clientele in detail
Should not have
• too colorful

```html
<!DOCTYPE html>
<html lang="en">
<head>
<meta charset="utf-8">
<title>Valtoni Business Card</title>
<link rel="stylesheet" href="https://fonts.googleapis.com/css2?family=Instrument+Sans:wght@400;500;700&display=swap">
<style>
  :root {
    --backdrop: #5f5f5f;
    --card: #ffffff;
    --accent: #e24a4e;
    --ink: #333333;
    --brand: #1d3f7e;
  }
  * { margin: 0; padding: 0; box-sizing: border-box; }
  html, body {
    width: 1200px;
    height: 1200px;
    overflow: hidden;
    background: var(--backdrop);
    font-family: "Instrument Sans", Arial, sans-serif;
  }
  .business-card {
    position: absolute;
    left: 169px;
    top: 349px;
    width: 861px;
    height: 502px;
    background: var(--card);
    border-radius: 36px;
    color: var(--ink);
  }
  .brand {
    position: absolute;
    left: 24px;
    top: 86px;
    display: flex;
    align-items: center;
    gap: 12px;
  }
  .brand-dot {
    width: 22px;
    height: 22px;
    border-radius: 50%;
    background: var(--brand);
  }
  .brand-name {
    font-size: 54px;
    font-weight: 700;
    color: var(--brand);
    line-height: 1;
  }
  .identity {
    position: absolute;
    left: 19px;
    top: 247px;
    padding-left: 16px;
    border-left: 4px solid var(--accent);
  }
  .person-name {
    font-size: 34px;
    font-weight: 500;
    color: var(--accent);
    line-height: 40px;
  }
  .person-role {
    font-size: 23px;
    line-height: 30px;
    margin-top: 2px;
  }
  .contact-list {
    position: absolute;
    left: 35px;
    top: 366px;
    list-style: none;
    font-size: 20px;
    line-height: 36px;
  }
  .contact-email { color: var(--accent); }
  .address {
    position: absolute;
    left: 492px;
    top: 405px;
    font-style: normal;
    font-size: 20px;
    line-height: 27px;
  }
</style>
</head>
<body>
  <div class="business-card">
    <div class="brand">
      <span class="brand-dot"></span>
      <span class="brand-name">Valtoni</span>
    </div>
    <div class="identity">
      <p class="person-name">Merenda Valtoni</p>
      <p class="person-role">Manager</p>
    </div>
    <ul class="contact-list">
      <li class="contact-phone">010 555 0182</li>
      <li class="contact-email">info@valtonipaint.co.za</li>
      <li class="contact-web">www.valtonipaint.co.za</li>
    </ul>
    <address class="address">
      14 Orion street<br>
      Northvale Benoni Gauteng 1520
    </address>
  </div>
</body>
</html>
```